Plastic Jar Catalogue 7

We are a plastic factory manufacturing different size of plastic jars, which mostly use for spice and grinded coffee. I need the catalogue to be 3 pages:First page: an attractive cover shows the factory's name and logo with a space for products’ picture. Second page: is an items page which I prefer to be enough for 4 items with a space for item number and description under each item. Last page: to be for factory’s address and contact details.

```html
<!DOCTYPE html>
<html lang="en">
<head>
<meta charset="utf-8">
<title>Clarity Jar Works – Catalogue</title>
<link rel="stylesheet" href="https://fonts.googleapis.com/css2?family=Open+Sans:wght@300;400;600&display=swap">
<style>
  :root {
    --board: #ebebeb;
    --paper: #f0f2f2;
    --teal-dark: #2596b1;
    --teal-mid: #3fa6c6;
    --sky: #62b7d8;
    --teal-pale: #86c6d3;
    --brand: #2a9bb5;
    --ink: #333a3d;
    --ink-soft: #4a4f52;
    --jar: #e2e6e9;
    --jar-edge: #c6ccd0;
    --bubble-a: #8fd0dc;
    --bubble-b: #4fb0c3;
  }
  * { margin: 0; padding: 0; box-sizing: border-box; }
  html, body { width: 1200px; height: 1200px; overflow: hidden; background: var(--board); }
  body { position: relative; font-family: "Open Sans", sans-serif; color: var(--ink); }

  .page {
    position: absolute;
    width: 656px; height: 464px;
    background: var(--paper);
    transform: scale(0.6204);
    transform-origin: 0 0;
    overflow: hidden;
  }
  .page--cover { left: 160px; top: 124px; }
  .page--items { left: 650px; top: 124px; }
  .page--contact { left: 371px; top: 492px; }

  /* Plain teal bands with a single soft arc edge */
  .band {
    position: absolute;
    border-radius: 50%;
  }
  .band--top { background: linear-gradient(90deg, var(--sky), var(--teal-mid) 55%, var(--teal-pale)); }
  .band--bottom { background: linear-gradient(90deg, var(--teal-pale), var(--teal-mid) 45%, var(--sky)); }

  .page--cover .band--top,
  .page--contact .band--top { left: -180px; top: -330px; width: 1016px; height: 470px; }
  .page--cover .band--bottom,
  .page--contact .band--bottom { left: -180px; top: 360px; width: 1016px; height: 420px; }
  .page--items .band--top { left: -160px; top: -400px; width: 976px; height: 460px; }
  .page--items .band--bottom { left: -160px; top: 410px; width: 976px; height: 400px; }

  .brand-name {
    position: absolute;
    color: var(--brand);
    font-weight: 600;
    text-transform: uppercase;
    text-align: center;
    letter-spacing: 5px;
    line-height: 1.3;
  }
  .page--cover .brand-name { left: 331px; top: 196px; width: 280px; font-size: 25px; }
  .page--contact .brand-name { left: 195px; top: 150px; width: 280px; font-size: 25px; }
  .page--items .brand-name { left: 2px; top: 362px; width: 96px; font-size: 9px; letter-spacing: 1.5px; }

  .product-photo {
    position: absolute;
    left: -45px; top: 128px;
    width: 285px; height: 285px;
    border-radius: 50%;
    background: radial-gradient(circle at 55% 55%, #f4f5f6 0%, #e4e7e9 60%, #cfd4d7 100%);
  }

  .cover-intro {
    position: absolute;
    left: 203px; top: 274px;
    width: 162px;
    text-align: right;
  }
  .cover-intro h2 { font-size: 14px; font-weight: 400; line-height: 18px; margin-bottom: 2px; }
  .cover-intro p { font-size: 8.2px; line-height: 11.1px; color: var(--ink-soft); }

  .item { position: absolute; }
  .item__jar {
    position: absolute;
    width: 80px; height: 120px;
    border-radius: 6px 6px 10px 10px;
    background: linear-gradient(90deg, var(--jar-edge) 0%, #f3f5f6 30%, var(--jar) 60%, var(--jar-edge) 100%);
  }
  .item__info {
    position: absolute;
    left: 70px; top: 14px;
    width: 106px; height: 106px;
    border-radius: 50%;
    background: radial-gradient(circle at 35% 30%, var(--bubble-a), var(--bubble-b));
    padding: 16px 12px 0 24px;
    color: #1f3a40;
  }
  .item__number { font-size: 9px; line-height: 11px; }
  .item__title { font-size: 10px; line-height: 12px; margin-bottom: 2px; }
  .item__desc { font-size: 5.6px; line-height: 7.3px; color: #24464d; }

  .item--1 { left: 60px; top: 95px; }
  .item--2 { left: 316px; top: 73px; }
  .item--3 { left: 174px; top: 265px; }
  .item--4 { left: 394px; top: 252px; }

  .contact {
    position: absolute;
    left: 128px; top: 252px;
    width: 400px;
    text-align: center;
  }
  .contact h2 { font-size: 19px; font-weight: 400; letter-spacing: 1px; line-height: 24px; margin-bottom: 2px; }
  .contact p { font-size: 12.5px; line-height: 18.5px; color: var(--ink); }

  .brief {
    position: absolute;
    left: 200px; top: 890px;
    width: 800px;
    text-align: center;
    font-weight: 300;
    font-size: 17.5px;
    line-height: 25px;
    letter-spacing: 2.3px;
    color: var(--ink-soft);
    white-space: nowrap;
  }
</style>
</head>
<body>

<!-- Cover -->
<section class="page page--cover">
  <div class="band band--top" role="img" aria-label="Decorative teal wave band"></div>
  <div class="band band--bottom" role="img" aria-label="Decorative teal wave band"></div>
  <div class="product-photo" role="img" aria-label="Product photo: clear plastic jars with round labels"></div>
  <div class="brand-name">Clarity Jar<br>Works</div>
  <div class="cover-intro">
    <h2>Lorem ipsum</h2>
    <p>dolor sit amet, consectetur<br>adipiscing elit. Pellentesque ege<br>stas felis turpis, sit amet rhoncus<br>augue gravida et. Aenean interdum<br>mattis sodales. Vivamus et tincidunt<br>neque. Integer sed viverra risus. Vesti<br>bulum ultrices sollicitudin magna, in<br>dignissim quam consequat ac. Vivamus<br>sit amet risus sed</p>
  </div>
</section>

<!-- Items -->
<section class="page page--items">
  <div class="band band--top" role="img" aria-label="Decorative teal wave band"></div>
  <div class="band band--bottom" role="img" aria-label="Decorative teal wave band"></div>

  <article class="item item--1">
    <div class="item__jar" role="img" aria-label="Product photo: clear plastic jar with lid"></div>
    <div class="item__info">
      <p class="item__number">#ProductNo</p>
      <p class="item__title">Lorem ipsum</p>
      <p class="item__desc">Clear PET jar with screw lid. Food safe for spice and coffee.</p>
    </div>
  </article>
  <article class="item item--2">
    <div class="item__jar" role="img" aria-label="Product photo: clear plastic jar with lid"></div>
    <div class="item__info">
      <p class="item__number">#ProductNo</p>
      <p class="item__title">Lorem ipsum</p>
      <p class="item__desc">Clear PET jar with screw lid. Food safe for spice and coffee.</p>
    </div>
  </article>
  <article class="item item--3">
    <div class="item__jar" role="img" aria-label="Product photo: clear plastic jar with lid"></div>
    <div class="item__info">
      <p class="item__number">#ProductNo</p>
      <p class="item__title">Lorem ipsum</p>
      <p class="item__desc">Clear PET jar with screw lid. Food safe for spice and coffee.</p>
    </div>
  </article>
  <article class="item item--4">
    <div class="item__jar" role="img" aria-label="Product photo: clear plastic jar with lid"></div>
    <div class="item__info">
      <p class="item__number">#ProductNo</p>
      <p class="item__title">Lorem ipsum</p>
      <p class="item__desc">Clear PET jar with screw lid. Food safe for spice and coffee.</p>
    </div>
  </article>

  <div class="brand-name">Clarity Jar<br>Works</div>
</section>

<!-- Contact -->
<section class="page page--contact">
  <div class="band band--top" role="img" aria-label="Decorative teal wave band"></div>
  <div class="band band--bottom" role="img" aria-label="Decorative teal wave band"></div>
  <div class="brand-name">Clarity Jar<br>Works</div>
  <div class="contact">
    <h2>ADDRES</h2>
    <p>dolor sit amet, consectetur adipiscing elit.<br>
    Pellentesque egestas felis turpis,<br>
    sit amet rhoncus augue gravida et.<br>
    Aenean interdum mattis sodales.</p>
  </div>
</section>

<p class="brief">We are a plastic factory manufacturing different size of plastic jars,<br>
which mostly use for spice and grinded coffee. I need the cata-<br>
logue to be 3 pages:First page: an attractive cover shows the facto-<br>
ry's name and logo with a space for products’ picture. Second<br>
page: is an items page which I prefer to be enough for 4 items with<br>
a space for item number and description under each item. Last<br>
page: to be for factory’s address and contact details.</p>

</body>
</html>
```